WP website design for Pelton

We need a wordpress design that will incorporate a professional color scheme with company logo in a clean layout. The design needs to consider that this will be developed on a responsive theme. Colors are will be the green of the logo and any others that will creatively highlight it.

Industry/Entity Type

It Company

Font styles to use
Sans Serif

Requirements
Must have
• Navigation: 1) Home 2) Auctions 3) Auction Services 4) Sellers 5) RK Pelton Livestock 6) About Us 7) Contact Us
Site will have slideshow element, image attached.
Widgets will be: 1)Email Signup form 2) Featured Auctions widget 3) Social Media (Chirply, Vidloop, RSS) 4) News & Events blog
Footer will have smaller company logo, association logos (attached) and contact info (below)
▪ R.K. Pelton Inc. / Auctioneers
▪ 4716 NC Hwy 91
▪ Marbury, NC 27604
▪ Office: (252) 555-0184
▪ Cell: (252) 555-0137
▪ email: rkpelton@rkpelton-example.com
Nice to have
• Site will have drop-down menus - please indicate the styling, for instance the dropdown menus

```html
<!DOCTYPE html>
<html lang="en">
<head>
<meta charset="utf-8">
<title>R.K. Pelton Inc. / Auctioneers</title>
<link href="https://fonts.googleapis.com/css2?family=Roboto:wght@400;500;700&display=swap" rel="stylesheet">
<style>
:root{
  --green:#3a8a1f;
  --green-dark:#2d7416;
  --green-light:#52a530;
  --text:#333;
  --muted:#666;
  --line:#d6d6d6;
  --footer:#efefef;
  --panel:#f5f4f4;
}
*{box-sizing:border-box;margin:0;padding:0}
html,body{width:1161px;height:1200px;overflow:hidden}
body{font-family:"Roboto",Arial,sans-serif;color:var(--text);background:#fff;position:relative}
.abs{position:absolute}
.top-bar{left:0;top:0;width:1161px;height:3px;background:var(--green)}
.header{left:0;top:3px;width:1161px;height:108px;background:linear-gradient(#fff,#ededed);border-bottom:1px solid #d9d9d9}
.brand{left:116px;top:38px;display:flex;align-items:center;gap:8px;font-size:26px;font-weight:500;color:var(--green)}
.brand .mark{width:22px;height:22px;border-radius:50%;background:var(--green)}
.brand small{display:block;font-size:14px;color:var(--green);font-weight:400}
.phone{left:888px;top:12px;display:flex;align-items:center;gap:10px;font-size:17px;font-weight:500;color:var(--green)}
.nav{left:374px;top:58px;display:flex;gap:0;font-size:13px}
.nav a{color:#222;text-decoration:none;padding:6px 17px;border-radius:3px;display:block}
.nav a.active{background:var(--green);color:#fff;box-shadow:0 2px 2px rgba(0,0,0,.25)}
.dropdown{left:516px;top:109px;width:164px;height:75px;background:var(--green);border-radius:3px;padding:9px 10px 0 24px;color:#fff;font-size:12.5px;line-height:19px;z-index:20;box-shadow:0 2px 3px rgba(0,0,0,.2)}
.dropdown:before{content:"";position:absolute;left:74px;top:-8px;border:8px solid transparent;border-top:0;border-bottom-color:var(--green)}
.dropdown li{list-style:disc}
.slider{left:116px;top:130px;width:928px;height:432px;background:#fff;border:1px solid #e2e2e2;z-index:1}
.slider-shadow{left:150px;top:560px;width:860px;height:14px;border-radius:50%;box-shadow:0 8px 10px rgba(0,0,0,.35)}
.slide{left:17px;top:15px;width:893px;height:402px;background:linear-gradient(#a9c7e6 0%,#8a6a3a 30%,#c98a3a 55%,#3a3426 70%,#7a5a30 85%,#3b4a30 100%)}
.arrow{top:206px;width:30px;height:30px;border-radius:50%;background:rgba(255,255,255,.85);display:flex;align-items:center;justify-content:center}
.caption{left:0;bottom:0;width:893px;height:78px;background:rgba(70,150,50,.82);color:#fff;padding:8px 28px}
.caption h2{font-size:21px;font-weight:400;margin-bottom:4px}
.caption p{font-size:11px;line-height:15px}
.section-title{font-size:23px;color:#555;display:flex;align-items:center;gap:10px}
.section-title span{color:var(--green)}
.title-icon{width:30px;height:30px;border-radius:7px;background:var(--green)}
.dash{height:0;border-top:1px dashed #ccc}
.auction-name{left:116px;top:669px;font-size:19px;color:#444}
.auction-name span{color:var(--green)}
.bidding{left:116px;top:696px;font-size:11px;color:#777}
.bidding span{color:var(--green)}
.thumb{top:722px;width:89px;height:89px;border:1px solid #ccc;padding:11px 1px;background:#fff}
.thumb div{width:100%;height:100%}
.tabs{left:117px;top:848px;width:579px;height:185px;background:var(--panel);box-shadow:0 1px 3px rgba(0,0,0,.25)}
.tab{top:0;height:38px;font-size:16px;display:flex;align-items:center;justify-content:center}
.tab.on{left:0;width:289px;background:linear-gradient(var(--green-light),var(--green-dark));color:#fff}
.tab.off{left:289px;width:290px;background:#e8e6e6;color:#555}
.news{top:60px;display:flex;gap:14px;width:285px}
.news .pic{width:93px;height:60px;background:linear-gradient(90deg,#6d5a3f,#2f4a3c 40%,#6a7a5a);flex:none}
.news .body{width:150px}
.news .date{display:inline-block;background:var(--green);color:#fff;font-size:12px;padding:1px 4px;margin-top:3px}
.news h4{font-weight:400;font-size:12px;margin:5px 0;color:#333;white-space:nowrap}
.news p{font-size:12px;line-height:16px}
.news a{color:var(--green);text-decoration:none}
.divider{left:747px;top:638px;width:1px;height:402px;background:linear-gradient(transparent,#ccc 20%,#ccc 80%,transparent)}
.input{left:800px;width:245px;height:28px;border:1px solid #ccc;font-size:11.5px;color:#777;padding:7px 10px;background:#fff}
.submit{left:803px;top:787px;width:67px;height:25px;border-radius:3px;background:linear-gradient(var(--green-light),var(--green-dark));color:#fff;font-size:12px;display:flex;align-items:center;justify-content:center}
.social{left:803px;width:242px;height:52px;border:1px solid #e0e0e0;display:flex;align-items:center;gap:6px;padding:0 10px;font-size:13px;font-weight:500;color:#444}
.social i{width:31px;height:31px;border-radius:4px;flex:none}
.icon-row{left:803px;top:1010px;display:flex;gap:5px}
.icon-row i{width:30px;height:30px;border-radius:4px;display:block}
.footer{left:0;top:1070px;width:1161px;height:126px;background:var(--footer)}
.footer-bar{left:0;top:1196px;width:1161px;height:4px;background:var(--green)}
.foot-brand{left:118px;top:1100px;font-size:22px;font-weight:500;color:#444;display:flex;align-items:center;gap:8px}
.foot-brand .mark{width:20px;height:20px;border-radius:50%;background:#444}
.foot-brand small{display:block;font-size:12px;font-weight:400}
.badge{top:1094px;background:#ddd}
.contact{top:1102px;font-size:11.5px;line-height:16.5px;color:#333;list-style:none}
.contact li:before{content:"▪ "}
</style>
</head>
<body>
<div class="abs top-bar"></div>
<header class="abs header"></header>
<div class="abs brand"><span class="mark"></span><div>R.K. Pelton<small>Inc. / Auctioneers</small></div></div>
<div class="abs phone">
  <svg width="22" height="22" viewBox="0 0 22 22"><circle cx="11" cy="11" r="10" fill="none" stroke="#222" stroke-width="1.6"/><path d="M7.5 6c.8-.5 1.6 0 2 1l.6 1.4c.2.5 0 1-.4 1.3l-.6.4c.5 1.2 1.3 2.1 2.4 2.6l.5-.6c.3-.4.9-.5 1.3-.3l1.4.7c.9.4 1.2 1.3.7 2-.9 1.2-2.7 1.3-4.6-.2-1.8-1.4-3.5-3.9-3.6-5.8 0-1.1.4-2 .3-2.5z" fill="#222"/></svg>
  (252) 555-0184
</div>
<nav class="abs nav">
  <a href="#">Home</a><a href="#">Auctions</a><a href="#" class="active">Auction Services</a><a href="#">Sellers</a><a href="#">RK Pelton Livestock</a><a href="#">About Us</a><a href="#">Contact Us</a>
</nav>

<div class="abs slider-shadow"></div>
<section class="abs slider">
  <div class="abs slide" role="img" aria-label="Autumn farmland with trees reflected in a pond">
    <div class="abs arrow" style="left:10px"><svg width="12" height="12" viewBox="0 0 12 12"><path d="M8 1L3 6l5 5" fill="none" stroke="#666" stroke-width="2.5"/></svg></div>
    <div class="abs arrow" style="right:10px"><svg width="12" height="12" viewBox="0 0 12 12"><path d="M4 1l5 5-5 5" fill="none" stroke="#666" stroke-width="2.5"/></svg></div>
    <div class="abs caption">
      <h2>Sed ut perspiciatis unde omnis iste natus error</h2>
      <p>vitae dicta sunt explicabo. Nemo enim ipsam voluptatem quia voluptas sit aspernatur aut odit aut fugit, sed quia consequuntur magni dolores eos qui ratione voluptatem sequi nesciunt. Neque porro quisquam est, qui dolorem ipsum quia dolor sit amet, consectetur, adipisci velit, sed quia non numquam</p>
    </div>
  </div>
</section>

<ul class="abs dropdown"><li>Submenu Here</li><li>Submenu Here</li><li>Submenu Here</li></ul>

<div class="abs section-title" style="left:118px;top:615px"><i class="title-icon"></i>Featured Auctions <span>widget</span></div>
<div class="abs dash" style="left:116px;top:655px;width:580px"></div>
<div class="abs auction-name"><span>Hobby</span> Farm Auction</div>
<div class="abs bidding">Bidding starts <span>march 14,2014 at 9:00am</span></div>
<div class="abs thumb" style="left:117px"><div role="img" aria-label="Cattle walking on a road" style="background:linear-gradient(#7e9a5c,#8a6d4a 65%,#9a9a9a)"></div></div>
<div class="abs thumb" style="left:215px"><div role="img" aria-label="Cattle walking on a road" style="background:linear-gradient(#7e9a5c,#8a6d4a 65%,#9a9a9a)"></div></div>
<div class="abs thumb" style="left:313px"><div role="img" aria-label="Herd of cattle in a pen" style="background:linear-gradient(#6a6a6a,#7a5a44)"></div></div>
<div class="abs thumb" style="left:411px"><div role="img" aria-label="Black cow in a pasture" style="background:linear-gradient(#c9b98a,#4a4a3a 50%,#a9a070)"></div></div>
<div class="abs thumb" style="left:510px"><div role="img" aria-label="Cattle in a dry field" style="background:linear-gradient(#aac4dc,#d4c090 60%,#c8b080)"></div></div>
<div class="abs thumb" style="left:608px"><div role="img" aria-label="Cattle grazing under trees" style="background:linear-gradient(#bcd0e0,#7a9a5a 55%,#5a7a3a)"></div></div>
<div class="abs dash" style="left:116px;top:833px;width:580px"></div>

<section class="abs tabs">
  <div class="abs tab on">Latest News</div>
  <div class="abs tab off">Blog</div>
  <article class="abs news" style="left:7px">
    <div class="pic" role="img" aria-label="Room with green walls"></div>
    <div class="body"><span class="date">12/8/2014</span><h4>Why Go for a Neutral Colour</h4><p>Are you looking for a simple yet elegant colour scheme for your walls?<br>................ <a href="#">see all</a></p></div>
  </article>
  <article class="abs news" style="left:304px">
    <div class="pic" role="img" aria-label="Room with green walls"></div>
    <div class="body"><span class="date">12/8/2014</span><h4>Why Go for a Neutral Colour</h4><p>Are you looking for a simple yet elegant colour scheme for your walls?<br>............... <a href="#">see all</a></p></div>
  </article>
</section>

<div class="abs divider"></div>

<div class="abs section-title" style="left:800px;top:607px;font-size:20px">
  <svg width="36" height="36" viewBox="0 0 36 36"><circle cx="18" cy="18" r="18" fill="#3a8a1f"/><rect x="9" y="12" width="18" height="12" fill="none" stroke="#fff" stroke-width="1.8"/><path d="M9 12l9 7 9-7" fill="none" stroke="#fff" stroke-width="1.8"/></svg>
  Email <span>Signup</span> form
</div>
<div class="abs dash" style="left:800px;top:651px;width:225px"></div>
<div class="abs input" style="top:665px">Name</div>
<div class="abs input" style="top:702px">Email</div>
<div class="abs input" style="top:740px">Phone</div>
<div class="abs submit">Submit</div>

<div class="abs social" style="top:825px">
  <i style="background:#f07a1c;display:flex;align-items:center;justify-content:center"><svg width="18" height="18" viewBox="0 0 18 18"><circle cx="3" cy="15" r="2.2" fill="#fff"/><path d="M1 8a9 9 0 0 1 9 9M1 2a15 15 0 0 1 15 15" fill="none" stroke="#fff" stroke-width="2.6"/></svg></i>
  Subscribe to our RSS Feeds!
</div>
<div class="abs social" style="top:887px"><i style="background:#7cc4e6"></i>Follow Us on Flitter!</div>
<div class="abs social" style="top:949px"><i style="background:#3b5b98"></i>Follow us on Chirply!</div>
<div class="abs icon-row">
  <i style="background:#5aaee0"></i><i style="background:#555"></i><i style="background:#3b5b98"></i><i style="background:#ccc"></i><i style="background:#2a8ac0"></i><i style="background:#b8d8ee"></i><i style="background:#3a9a3a"></i>
</div>

<footer class="abs footer"></footer>
<div class="abs foot-brand"><span class="mark"></span><div>R.K. Pelton<small>Inc. / Auctioneers</small></div></div>
<div class="abs badge" style="left:300px;width:88px;height:60px;top:1100px;background:#d8d8d8"></div>
<div class="abs badge" style="left:421px;width:75px;height:62px;top:1098px;background:#e3d4d6"></div>
<div class="abs badge" style="left:520px;width:74px;height:74px;border-radius:50%;background:#cfd8cc"></div>
<ul class="abs contact" style="left:695px">
  <li>R.K. Pelton Inc. / Auctioneers</li><li>4716 NC Hwy 91</li><li>Marbury, NC 27604</li>
</ul>
<ul class="abs contact" style="left:880px">
  <li>Office: (252) 555-0184</li><li>Cell: (252) 555-0137</li><li>email: rkpelton@rkpelton-example.com</li>
</ul>
<div class="abs footer-bar"></div>
</body>
</html>
```